Natural deodorant label

Natural clean deodorant line. Need modernize label which can be sized for both the regular and travel size deodorants. 2.75 x 3" and 1x2". Important to highlight no baking soda and its natural. Also has no aluminum, preservatives, nor chemicals. Its gender inclusive and safe for all ages. Please see website at www.lorvatique.com. will attach current label. Will need a label that i would be able to update with new scents as they come. Want a clean look.
Updates

Need extra days to review

Target Market(s)

the working mother/wife that lives a clean healthy life and pushes that for her family

Industry/Entity Type

health and beauty/deodorant/natural

Colors

Designer to choose colors to be used in the design.

Requirements
Must have
• No baking soda and gender inclusive on label. Clean look. Very little to no picture art.
Nice to have
• Potentially a different color representing the different scents. A brief description of the deodorant scent underneath the scent name. This can be found under the drop down menu titled valdora deodorant scents on the website www.lorvatique.com. Area on front label for a small barcode.
Should not have
• misspelled words; dark label

```html
<!DOCTYPE html>
<html lang="en">
<head>
<meta charset="utf-8">
<title>Lorvatique — Valdora Solstice Deodorant Label</title>
<link rel="stylesheet" href="https://fonts.googleapis.com/css2?family=Cinzel:wght@600&family=EB+Garamond&family=Great+Vibes&family=Norican&family=Open+Sans:ital,wght@1,600;1,700;1,800&family=Poppins:wght@600&display=swap">
<style>
  :root {
    --page: #ffffff;
    --label-light: #fcfbf9;
    --label-tint: #f1efea;
    --blush: #f7e3df;
    --frame: #ee7b7b;
    --accent: #e8455c;
    --accent-text: #e0263c;
    --ink: #111111;
    --on-accent: #ffffff;
  }
  * { margin: 0; padding: 0; box-sizing: border-box; }
  html, body {
    width: 1200px;
    height: 1200px;
    overflow: hidden;
    background: var(--page);
  }
  .sheet {
    position: relative;
    width: 1200px;
    height: 1200px;
  }
  .label {
    position: absolute;
    top: 100px;
    width: 500px;
    height: 1000px;
    box-shadow: 0 6px 22px rgba(0, 0, 0, 0.12);
  }
  .label--front { left: 70px; }
  .label--back { left: 630px; }
  .label svg { display: block; width: 100%; height: 100%; }

  .frame { fill: rgba(255, 255, 255, 0.55); stroke: var(--frame); stroke-width: 6; }
  .brand-dot { fill: var(--ink); }
  .brand-name { font-family: "Cinzel", serif; font-weight: 600; font-size: 40px; fill: var(--ink); letter-spacing: 1px; }
  .scent-line { font-family: "Great Vibes", cursive; font-size: 74px; fill: var(--ink); }
  .scent-rule { fill: var(--ink); }
  .scent-name { font-family: "Poppins", sans-serif; font-weight: 600; font-size: 78px; fill: var(--ink); letter-spacing: -3px; }
  .tagline { font-family: "Norican", cursive; font-size: 48px; fill: var(--ink); }
  .net-weight { font-family: "EB Garamond", serif; font-size: 34px; fill: var(--ink); }
  .claim { font-family: "Open Sans", sans-serif; font-style: italic; font-weight: 700; font-size: 23px; fill: var(--accent-text); }
  .panel { fill: var(--accent); }
  .panel-title { font-family: "Open Sans", sans-serif; font-style: italic; font-weight: 700; font-size: 32px; fill: var(--on-accent); }
  .panel-note { font-family: "Open Sans", sans-serif; font-style: italic; font-weight: 600; font-size: 22px; fill: var(--on-accent); }
  .ingredients { font-family: "Open Sans", sans-serif; font-style: italic; font-weight: 700; font-size: 31px; fill: var(--on-accent); }
  .footer-note { font-family: "Open Sans", sans-serif; font-style: italic; font-weight: 600; font-size: 30px; fill: var(--ink); }
  .footer-web { font-family: "Open Sans", sans-serif; font-style: italic; font-weight: 700; font-size: 29px; fill: var(--ink); }
</style>
</head>
<body>
<main class="sheet">

  <figure class="label label--front">
    <svg viewBox="0 0 500 1000" xmlns="http://www.w3.org/2000/svg">
      <defs>
        <linearGradient id="label-wash" x1="0" y1="0" x2="1" y2="1">
          <stop offset="0" stop-color="var(--label-tint)"/>
          <stop offset="0.35" stop-color="var(--label-light)"/>
          <stop offset="0.7" stop-color="var(--blush)" stop-opacity="0.5"/>
          <stop offset="1" stop-color="var(--label-tint)"/>
        </linearGradient>
      </defs>
      <rect class="label-backdrop" width="500" height="1000" fill="url(#label-wash)" role="img" aria-label="Faint botanical pattern of leaves and small peach blossoms"/>
      <path class="frame" d="M64,105 H140 Q154,105 154,90 V60 Q154,22 192,22 H298 Q336,22 336,60 V90 Q336,105 350,105 H433 Q478,105 478,150 V923 Q478,968 433,968 H64 Q19,968 19,923 V150 Q19,105 64,105 Z"/>
      <circle class="brand-dot" cx="245" cy="105" r="40"/>
      <text class="brand-name" x="250" y="206" text-anchor="middle">LORVATIQUE</text>
      <text class="scent-line" x="250" y="412" text-anchor="middle">Valdora</text>
      <rect class="scent-rule" x="44" y="437" width="416" height="5"/>
      <text class="scent-name" x="250" y="520" text-anchor="middle">Solstice</text>
      <text class="tagline" x="100" y="722">Naturally</text>
      <text class="tagline" x="155" y="772">Refreshing</text>
      <text class="net-weight" x="250" y="832" text-anchor="middle">NET WT 2.5 OZ (70G)</text>
      <text class="claim" x="250" y="926" text-anchor="middle">No baking soda &amp; gender inclusive</text>
    </svg>
  </figure>

  <figure class="label label--back">
    <svg viewBox="0 0 500 1000" xmlns="http://www.w3.org/2000/svg">
      <defs>
        <linearGradient id="label-wash-back" x1="0" y1="0" x2="1" y2="1">
          <stop offset="0" stop-color="var(--blush)" stop-opacity="0.6"/>
          <stop offset="0.3" stop-color="var(--label-light)"/>
          <stop offset="0.75" stop-color="var(--label-tint)"/>
          <stop offset="1" stop-color="var(--label-light)"/>
        </linearGradient>
      </defs>
      <rect class="label-backdrop" width="500" height="1000" fill="url(#label-wash-back)" role="img" aria-label="Faint botanical pattern of leaves and small peach blossoms"/>
      <path class="frame" d="M64,105 H140 Q154,105 154,90 V60 Q154,22 192,22 H298 Q336,22 336,60 V90 Q336,105 350,105 H433 Q478,105 478,150 V918 Q478,963 433,963 H64 Q19,963 19,918 V150 Q19,105 64,105 Z"/>
      <circle class="brand-dot" cx="245" cy="90" r="40"/>
      <text class="brand-name" x="250" y="193" text-anchor="middle">LORVATIQUE</text>

      <rect class="panel" x="33" y="270" width="424" height="159" rx="22"/>
      <text class="panel-title" x="245" y="307" text-anchor="middle">100% ORGANIC</text>
      <text class="panel-title" x="245" y="338" text-anchor="middle">ALUMINUM FREE</text>
      <text class="panel-title" x="245" y="371" text-anchor="middle">UNISEX DEODORANT</text>
      <text class="panel-note" x="245" y="401" text-anchor="middle">No baking soda &amp; gender inclusive</text>

      <rect class="panel" x="42" y="443" width="415" height="371" rx="22"/>
      <text class="ingredients" text-anchor="middle">
        <tspan x="250" y="491">Ingredients: Raw</tspan>
        <tspan x="250" y="530">alkaline coconut oil,</tspan>
        <tspan x="250" y="569">Mango butter,</tspan>
        <tspan x="250" y="608">arrowroot powder,</tspan>
        <tspan x="250" y="647">candelilla wax, zinc</tspan>
        <tspan x="250" y="686">ricinoleate, zinc</tspan>
        <tspan x="250" y="725">powder, vitamin E</tspan>
        <tspan x="250" y="764">oil, fragrance.</tspan>
      </text>

      <text class="footer-note" x="250" y="873" text-anchor="middle">Cruelty free Vegan</text>
      <text class="footer-web" x="250" y="916" text-anchor="middle">WWW.LORVATIQUE.COM</text>
    </svg>
  </figure>

</main>
</body>
</html>
```